Valiant Sons Ministry - 3

Features of prayer:
- Prayer should be out of a filial relationship with the Father. Heb. 5:7
- Prayer is a divine responsibility to walk and work with God. Col. 1:10, 1 Cor. 15:58
- Prayer should depend on the Holy Spirit: Rom. 8:26-27, Jude 1:20
- Prayer should be effective and fervent: James 5:16, Luke 22:44
- Prayer should be word based: Acts 4:23-33
- Prayer should demonstrate faith: Matt. 21:22
- Prayer should proceed from a heart of worship: Phil. 4:6
- Time is of essence in prayer: Luke 6:12
- Prayer requires you as a whole: Acts 6:4, Rom. 12:1
- You learn how to pray by praying: Luke 11:2

You learn how to pray by praying
"Men ought always to pray and not to faint"

Join the Valiant Sons Ministry!

Ministry

```html
<!DOCTYPE html>
<html lang="en">
<head>
<meta charset="utf-8">
<title>Join the Valiant Sons Ministry</title>
<link rel="stylesheet" href="https://fonts.googleapis.com/css2?family=Pinyon+Script&family=Gentium+Book+Plus:ital,wght@0,400;0,700;1,400;1,700&display=swap">
<style>
  :root {
    --frame: #aeb9c6;
    --sky-top: #e4ecee;
    --sky-mid: #f3f7f6;
    --sky-low: #e2ebee;
    --navy: #1e2d63;
    --ink: #121418;
    --rule: #8a96a8;
    --photo-light: #e9eef0;
    --photo-mid: #b9b4ad;
    --photo-dark: #6f6862;
  }
  * { margin: 0; padding: 0; box-sizing: border-box; }
  html, body { width: 848px; height: 1200px; overflow: hidden; background: var(--frame); }
  .poster {
    position: relative;
    width: 848px; height: 1200px;
    background: var(--frame);
    font-family: "Gentium Book Plus", "Palatino Linotype", serif;
  }
  .sheet {
    position: absolute; inset: 9px;
    border-radius: 22px;
    overflow: hidden;
    background:
      radial-gradient(ellipse 60% 30% at 50% 8%, #ffffff 0%, rgba(255,255,255,0) 70%),
      linear-gradient(180deg, var(--sky-top) 0%, var(--sky-mid) 30%, var(--sky-low) 65%, #edf1f1 100%);
  }
  .brand {
    position: absolute; top: 82px; left: 0; right: 0;
    display: flex; align-items: center; justify-content: center; gap: 16px;
  }
  .brand-mark {
    width: 72px; height: 72px; border-radius: 50%;
    border: 5px solid var(--navy);
  }
  .brand-name {
    font-size: 30px; font-weight: 400; color: var(--navy);
    line-height: 1.1;
  }
  .headline {
    position: absolute; top: 196px; left: 0; right: 0;
    text-align: center;
    font-family: "Pinyon Script", cursive;
    color: var(--navy);
    font-weight: 400;
    line-height: 1;
  }
  .headline .lead { display: block; font-size: 60px; }
  .headline .name { display: block; font-size: 66px; margin-top: 2px; }
  .headline-rule {
    position: absolute; top: 339px; left: 70px; right: 70px;
    border-top: 1px dotted var(--rule);
  }
  .intro {
    position: absolute; top: 380px; left: 0; right: 0;
    text-align: center; color: var(--ink);
    font-style: italic; font-weight: 700;
    font-size: 24.5px; line-height: 30px;
  }
  .features {
    position: absolute; top: 460px; left: 20px; right: 20px;
    text-align: center; color: var(--ink);
  }
  .features h2 {
    font-size: 21.5px; font-style: italic; font-weight: 700;
    line-height: 28px; margin-bottom: 2px;
  }
  .features ul { list-style: none; }
  .features li { font-size: 19.5px; line-height: 30.2px; }
  .photo {
    position: absolute; left: 0; right: 0; top: 780px; bottom: 0;
    background:
      radial-gradient(ellipse 32% 48% at 64% 62%, var(--photo-mid) 0%, rgba(185,180,173,0.6) 45%, rgba(185,180,173,0) 75%),
      radial-gradient(ellipse 30% 40% at 20% 85%, #d6d9da 0%, rgba(214,217,218,0) 70%),
      linear-gradient(180deg, rgba(233,238,240,0) 0%, var(--photo-light) 25%, #d4d6d6 100%);
  }
  .photo::after {
    content: ""; position: absolute; left: 50%; top: 30%; width: 34%; height: 70%;
    background: radial-gradient(ellipse at 40% 60%, rgba(111,104,98,0.55), rgba(111,104,98,0) 70%);
  }
</style>
</head>
<body>
<div class="poster">
  <div class="sheet">
    <header class="brand">
      <span class="brand-mark"></span>
      <span class="brand-name">Brothers in Worship Fellowship</span>
    </header>

    <h1 class="headline">
      <span class="lead">Join the</span>
      <span class="name">Valiant Sons Ministry!</span>
    </h1>
    <div class="headline-rule"></div>

    <p class="intro">You learn how to pray by praying<br>“Men ought always to pray and not to faint”</p>

    <section class="features">
      <h2>Features of prayer:</h2>
      <ul>
        <li>Prayer should be out of a filial relationship with the Father. Heb. 5:7</li>
        <li>Prayer is a divine responsibility to walk and work with God. Col. 1:10, 1 Cor. 15:58</li>
        <li>Prayer should depend on the Holy Spirit: Rom. 8:26-27, Jude 1:20</li>
        <li>Prayer should be effective and fervent: James 5:16, Luke 22:44</li>
        <li>Prayer should be word based: Acts 4:23-33</li>
        <li>Prayer should demonstrate faith: Matt. 21:22</li>
        <li>Prayer should proceed from a heart of worship: Phil. 4:6</li>
        <li>Time is of essence in prayer: Luke 6:12</li>
        <li>Prayer requires you as a whole: Acts 6:4, Rom. 12:1</li>
        <li>You learn how to pray by praying: Luke 11:2</li>
      </ul>
    </section>

    <div class="photo" role="img" aria-label="Photograph of clasped hands in prayer resting beside an open Bible"></div>
  </div>
</div>
</body>
</html>
```